VONTRA - Visual Orbit Networked Trade Arrangement - business cards

3x3 inch business cards
full color
use attached logo with old business card info

VONTRA will design, integrate and manufacture equipment for you to create an engaging, impactful experience for you and your consumer.

MISSION
VONTRA creates content-rich, emotionally compelling, and experiential spaces for a wide range of environments. Helping people find their way, communicate important information, and create unique moment of impact in virtually any environment that communicate with users.

What
You name it we will develop it, from digital wayfinding signage, multimedia installations, user interfaces, in any environment. We strive to enrich the lives of people wherever they work, play, learn, shop, travel, or gather.

HOW
We plan, design, and build a diverse range of visual communication and information systems, to improve the human experience. Dedicated to a collaborative design process that puts user needs first. We work with your ideas to shape a unique user experience that orients, informs, educates and captivates.
Benefits
Improved customer experience
Improved Branding/recall
Sales Lift
Cost savings/efficiency
Ad revenue/ROI
Differentiator from competition
Reduce perceived wait times
Internal communication
Generate inquiries
Safety/security
Better compliance/display control
Responsiveness
Public information
WHERE
Shopping Malls, entertainment and hospitality destinations and other environments are using the tools and story-telling approaches to create more engaging, emotionally compelling and impactful interactions with their customers, guests and users.
Markets
Architectural
Corporate
Education
Entertainment
Exhibition
Government
Healthcare
Hospitality
Residential
Retail
Sports
Tourism
Transportation
Urban
Visitor Centers
Workplace

Target Market(s)

corporate B2B, see attached details

Industry/Entity Type

Digital Signage

Contact Information for Business Card

see personal details from Pellward business cards apply to new cards

but use

www.vontra-example.com
marla@vontra-example.com

Font styles to use
Other font styles liked:
• century gothic

Colors
0355a3
3277b5
85acd3
34a6d7
0692cd

Requirements
Must have
• existing logo
• want depth and impact from the cards.
• giant dice image on one side of card
• details on the front side of card
• scalable image so you read the words under the logo
• 3inch x 3inch size only
Nice to have
• watermark with big dice image on front or possibly on the back with the cull logo on top of watermark cube.
• same blue color font on logo as on the card
• could use word cloud on the back of card (these are our company values)
Should not have
• should not be blank 2nd side
• should not just/ only redo my attachments - they are only a concept not what I want that's why I am using your services to provide more creativity and better ideas.

```html
<!DOCTYPE html>
<html lang="en">
<head>
<meta charset="utf-8">
<title>VONTRA business cards</title>
<link href="https://fonts.googleapis.com/css2?family=PT+Sans:ital,wght@0,400;0,700;1,400&display=swap" rel="stylesheet">
<style>
  :root {
    --stage: #161618;
    --card: #ffffff;
    --name-blue: #1b8fd8;
    --text-blue: #1e7fc6;
    --brand-blue: #1c5e9f;
    --wash-blue: #d6e7f5;
    --wash-blue-mid: #e6f0f9;
  }
  * { box-sizing: border-box; margin: 0; padding: 0; }
  html, body {
    width: 1200px;
    height: 873px;
    overflow: hidden;
    background: var(--stage);
    font-family: "PT Sans", sans-serif;
  }
  .sheet {
    width: 1200px;
    height: 873px;
    display: flex;
    align-items: center;
    justify-content: center;
    gap: 64px;
  }
  .card {
    position: relative;
    width: 420px;
    height: 420px;
    background: var(--card);
    border-radius: 3px;
    box-shadow: 0 10px 30px rgba(0,0,0,.5);
    overflow: hidden;
  }

  /* Contact side */
  .card-front { padding: 36px 30px; }
  .person-name {
    font-weight: 700;
    font-size: 38px;
    line-height: 1;
    color: var(--name-blue);
  }
  .person-title {
    font-style: italic;
    font-size: 13.5px;
    color: var(--text-blue);
    margin-top: 8px;
  }
  .contact-list {
    list-style: none;
    margin-top: 24px;
  }
  .contact-item {
    display: flex;
    align-items: center;
    gap: 12px;
    font-size: 15px;
    line-height: 26px;
    color: var(--text-blue);
    white-space: nowrap;
  }
  .contact-icon {
    width: 14px;
    height: 14px;
    flex: none;
    fill: var(--text-blue);
    stroke: var(--text-blue);
  }

  .brand {
    position: absolute;
    display: flex;
    flex-direction: column;
    align-items: flex-start;
    color: var(--brand-blue);
  }
  .brand-row { display: flex; align-items: center; gap: 10px; }
  .brand-dot {
    width: 22px;
    height: 22px;
    border-radius: 50%;
    background: var(--brand-blue);
  }
  .brand-name {
    font-weight: 400;
    font-size: 40px;
    line-height: 1;
    letter-spacing: 1px;
  }
  .brand-tagline {
    font-size: 6.5px;
    letter-spacing: .3px;
    text-transform: uppercase;
    margin: 3px 0 0 32px;
  }
  .card-front .brand { right: 30px; bottom: 40px; }

  /* Brand side */
  .watermark {
    position: absolute;
    right: -50px;
    bottom: -50px;
    width: 400px;
    height: 340px;
    border-radius: 46% 54% 50% 50%;
    background: radial-gradient(ellipse at 45% 45%, var(--wash-blue) 0%, var(--wash-blue-mid) 55%, rgba(255,255,255,0) 76%);
  }
  .card-back .brand { left: 48px; top: 60px; z-index: 1; }
  .card-back .brand-name { font-size: 46px; }
  .card-back .brand-dot { width: 26px; height: 26px; }
  .card-back .brand-tagline { font-size: 7px; margin-left: 36px; }
</style>
</head>
<body>
<main class="sheet">

  <section class="card card-front" aria-label="Business card, contact side">
    <h1 class="person-name">Marla Quenby</h1>
    <p class="person-title">Director, Organizational &amp; Business Improvement</p>
    <ul class="contact-list">
      <li class="contact-item">
        <svg class="contact-icon" viewBox="0 0 14 14" aria-hidden="true"><rect x="2" y="2" width="10" height="10" fill="none" stroke-width="1.4"/></svg>
        555.014.2200
      </li>
      <li class="contact-item">
        <svg class="contact-icon" viewBox="0 0 14 14" aria-hidden="true"><path d="M3 1.5 L5.5 1.5 L6.5 4.5 L5 5.8 C5.8 7.6 6.6 8.4 8.2 9.2 L9.5 7.7 L12.5 8.7 L12.5 11.2 C12.5 12 11.8 12.6 11 12.5 C6 12 2 8 1.5 3 C1.4 2.2 2.1 1.5 3 1.5 Z" stroke="none"/></svg>
        555.014.2200 x 116
      </li>
      <li class="contact-item">
        <svg class="contact-icon" viewBox="0 0 14 14" aria-hidden="true"><rect x="1" y="3" width="12" height="8.5" stroke="none"/><path d="M1 3 L7 8 L13 3" fill="none" stroke="#fff" stroke-width="1.2"/></svg>
        marla@vontra-example.com
      </li>
      <li class="contact-item">
        <svg class="contact-icon" viewBox="0 0 14 14" aria-hidden="true"><circle cx="7" cy="7" r="6" stroke="none"/><path d="M1 7 H13 M7 1 C4 4 4 10 7 13 M7 1 C10 4 10 10 7 13" fill="none" stroke="#fff" stroke-width="1"/></svg>
        www.vontra-example.com
      </li>
      <li class="contact-item">
        <svg class="contact-icon" viewBox="0 0 14 14" aria-hidden="true"><path d="M7 13 C7 13 2.5 8 2.5 5.3 A4.5 4.5 0 0 1 11.5 5.3 C11.5 8 7 13 7 13 Z" stroke="none"/><circle cx="7" cy="5.3" r="1.6" fill="#fff" stroke="none"/></svg>
        4820-18 Street, Northgate, ZZ 0A0 0A0 Canada
      </li>
    </ul>
    <div class="brand">
      <div class="brand-row"><span class="brand-dot"></span><span class="brand-name">VONTRA</span></div>
      <span class="brand-tagline">Visual Orbit Networked Trade Arrangement</span>
    </div>
  </section>

  <section class="card card-back" aria-label="Business card, brand side">
    <div class="watermark" role="img" aria-label="Giant faint dice image in pale blue as a watermark"></div>
    <div class="brand">
      <div class="brand-row"><span class="brand-dot"></span><span class="brand-name">VONTRA</span></div>
      <span class="brand-tagline">Visual Orbit Networked Trade Arrangement</span>
    </div>
  </section>

</main>
</body>
</html>
```